Boilerplate Management Organization Chart

"Our Management Approach is a deliberate step-by-step process and supports our Technical Approach detailed in proposal submission. The Management Approach covers all the human capital aspects for executing a contract—from contract award through to sustainment and/or transition of the contract to another company. It includes how we organize, hire, staff, train, and account for our contract employees—as well as their complete personal life-cycle management within the company."

We need this management approach to depict an amazing management process that demonstrates best practices of the project management body of knowledge. We need this vector image to be applicable to any proposal without making references to any other proposals. Generic names but using strong business language.
Updates

Thanks for all designs submitted thus far. Some have stuck to the original type of chart. We would like to see a completely different way to show the same information. It has to be able to be recognized and deciphered very quickly by people who might not necessarily want to look at it. It must draw them in and make it incredibly easy to distinguish a management approach that looks fresh, infallible, and easily implemented.

Target Market(s)

Federal space, Government organizations looking for procedural efficiencies,

Industry/Entity Type

Management

Requirements
Must have
• Must not take up more than 1/3 to 1/2 of printable page and be clear.
Should not have
• Not too much color, but should stick to some color palette of some interest.

```html
<!DOCTYPE html>
<html lang="en">
<head>
<meta charset="utf-8">
<title>Management Approach – Program Evaluation</title>
<link rel="stylesheet" href="https://fonts.googleapis.com/css2?family=Roboto+Condensed:wght@700&display=swap">
<style>
  :root {
    --sustain: #a51d39;
    --sustain-dark: #7a1428;
    --responsibility: #f05d60;
    --responsibility-dark: #c94346;
    --oversight: #eeae4e;
    --oversight-dark: #b87a2c;
    --manning: #a3cb5c;
    --manning-dark: #6f9640;
    --training: #1bcb9d;
    --training-dark: #0f8666;
    --development: #2b9fad;
    --development-dark: #1b5e6a;
    --benefits: #3a4240;
    --benefits-dark: #1f2524;
    --retention: #626a67;
    --retention-dark: #3d4442;
    --panel-fill: #ededed;
    --panel-line: #d4d4d4;
    --label-grey: #7a7a7a;
    --white: #ffffff;
  }
  html, body {
    margin: 0;
    padding: 0;
    width: 1200px;
    height: 1200px;
    overflow: hidden;
    background: var(--white);
  }
  .approach-graphic {
    display: block;
    width: 1200px;
    height: 1200px;
    font-family: "Roboto Condensed", "Arial Narrow", sans-serif;
    font-weight: 700;
  }
  .segment-label {
    fill: var(--white);
    font-size: 34px;
    text-anchor: middle;
  }
  .segment-icon {
    fill: none;
    stroke: var(--white);
    stroke-width: 6;
    stroke-linecap: round;
    stroke-linejoin: round;
  }
  .segment-icon-solid { fill: var(--white); stroke: none; }
  .tag-box {
    fill: var(--white);
    stroke: var(--panel-line);
    stroke-width: 5;
  }
  .tag-text {
    fill: var(--label-grey);
    text-anchor: middle;
  }
</style>
</head>
<body>
<svg class="approach-graphic" viewBox="0 0 1300 1300" xmlns="http://www.w3.org/2000/svg">
  <defs>
    <linearGradient id="grad-sustain" x1="0" y1="1" x2="1" y2="0"><stop offset="0" style="stop-color:var(--sustain-dark)"/><stop offset="1" style="stop-color:var(--sustain)"/></linearGradient>
    <linearGradient id="grad-responsibility" x1="0" y1="0" x2="1" y2="0"><stop offset="0" style="stop-color:var(--responsibility-dark)"/><stop offset="0.4" style="stop-color:var(--responsibility)"/></linearGradient>
    <linearGradient id="grad-oversight" x1="0" y1="0" x2="1" y2="1"><stop offset="0" style="stop-color:var(--oversight-dark)"/><stop offset="0.6" style="stop-color:var(--oversight)"/></linearGradient>
    <linearGradient id="grad-manning" x1="1" y1="0" x2="0" y2="1"><stop offset="0" style="stop-color:var(--manning-dark)"/><stop offset="0.5" style="stop-color:var(--manning)"/></linearGradient>
    <linearGradient id="grad-training" x1="0" y1="0" x2="1" y2="1"><stop offset="0.3" style="stop-color:var(--training)"/><stop offset="1" style="stop-color:var(--training-dark)"/></linearGradient>
    <linearGradient id="grad-development" x1="0" y1="0" x2="1" y2="0"><stop offset="0.2" style="stop-color:var(--development)"/><stop offset="1" style="stop-color:var(--development-dark)"/></linearGradient>
    <linearGradient id="grad-benefits" x1="0" y1="0" x2="1" y2="1"><stop offset="0" style="stop-color:var(--benefits)"/><stop offset="1" style="stop-color:var(--benefits-dark)"/></linearGradient>
    <linearGradient id="grad-retention" x1="0" y1="0" x2="0" y2="1"><stop offset="0" style="stop-color:var(--retention)"/><stop offset="1" style="stop-color:var(--retention-dark)"/></linearGradient>
  </defs>

  <!-- backing panel -->
  <rect class="backing-panel" x="158" y="170" width="1040" height="888" rx="32" fill="var(--panel-fill)" stroke="var(--panel-line)" stroke-width="6"/>

  <!-- pointer toward the wheel -->
  <polygon class="approach-pointer" points="730,222 775,190 775,208 870,208 870,236 775,236 775,254" fill="var(--panel-line)"/>

  <!-- wheel segments -->
  <g class="wheel">
    <path class="segment segment-sustainment" fill="url(#grad-sustain)" d="M423.5,457.5 L231.1,265.1 A417,417 0 0 1 526,143 L526,415 A145,145 0 0 0 423.5,457.5 Z"/>
    <path class="segment segment-responsibility" fill="url(#grad-responsibility)" d="M526,415 L526,160 A400,400 0 0 1 808.8,277.2 L628.5,457.5 A145,145 0 0 0 526,415 Z"/>
    <path class="segment segment-oversight" fill="url(#grad-oversight)" d="M628.5,457.5 L820.9,265.1 A417,417 0 0 1 943,560 L671,560 A145,145 0 0 0 628.5,457.5 Z"/>
    <path class="segment segment-manning" fill="url(#grad-manning)" d="M671,560 L931,560 A405,405 0 0 1 812.4,846.4 L628.5,662.5 A145,145 0 0 0 671,560 Z"/>
    <path class="segment segment-training" fill="url(#grad-training)" d="M628.5,662.5 L820.9,854.9 A417,417 0 0 1 526,977 L526,705 A145,145 0 0 0 628.5,662.5 Z"/>
    <path class="segment segment-development" fill="url(#grad-development)" d="M526,705 L526,965 A405,405 0 0 1 239.6,846.4 L423.5,662.5 A145,145 0 0 0 526,705 Z"/>
    <path class="segment segment-benefits" fill="url(#grad-benefits)" d="M423.5,662.5 L231.1,854.9 A417,417 0 0 1 109,560 L381,560 A145,145 0 0 0 423.5,662.5 Z"/>
    <path class="segment segment-retention" fill="url(#grad-retention)" d="M381,560 L121,560 A405,405 0 0 1 239.6,273.6 L423.5,457.5 A145,145 0 0 0 381,560 Z"/>
  </g>

  <!-- hub ring -->
  <g class="hub-ring" fill="none" stroke-width="20">
    <path stroke="var(--sustain)" d="M438.3,472.3 A124,124 0 0 1 526,436"/>
    <path stroke="var(--responsibility)" d="M526,436 A124,124 0 0 1 613.7,472.3"/>
    <path stroke="var(--oversight)" d="M613.7,472.3 A124,124 0 0 1 650,560"/>
    <path stroke="var(--manning)" d="M650,560 A124,124 0 0 1 613.7,647.7"/>
    <path stroke="var(--training)" d="M613.7,647.7 A124,124 0 0 1 526,684"/>
    <path stroke="var(--development)" d="M526,684 A124,124 0 0 1 438.3,647.7"/>
    <path stroke="var(--benefits)" d="M438.3,647.7 A124,124 0 0 1 402,560"/>
    <path stroke="var(--retention)" d="M402,560 A124,124 0 0 1 438.3,472.3"/>
  </g>

  <!-- icons -->
  <g class="segment-icon icon-transition">
    <circle cx="410" cy="240" r="22"/><circle cx="436" cy="222" r="22"/>
    <path d="M408,246 L438,216 M426,216 L438,216 L438,228"/>
  </g>
  <g class="segment-icon icon-handshake">
    <path d="M600,222 L615,212 L640,226 L660,214 L676,224 M600,222 L608,246 L640,266 L676,240 L676,224 M624,238 L640,252 M632,232 L650,246"/>
    <path d="M598,214 L586,244 M678,214 L692,244"/>
  </g>
  <g class="segment-icon icon-oversight">
    <circle cx="752" cy="408" r="28"/>
    <path d="M740,398 h6 M752,398 h14 M740,414 h6 M752,414 h14"/>
    <circle class="segment-icon-solid" cx="790" cy="390" r="15"/>
    <path d="M783,390 l5,5 l9,-10" stroke="var(--oversight)" stroke-width="4"/>
  </g>
  <g class="segment-icon icon-team">
    <circle cx="766" cy="598" r="9"/><circle cx="792" cy="594" r="11"/><circle cx="818" cy="598" r="9"/>
    <path d="M748,624 q18,-18 36,0 M774,628 q18,-22 36,0 M800,624 q18,-18 36,0"/>
  </g>
  <g class="segment-icon icon-training">
    <rect x="622" y="746" width="36" height="34" rx="2"/>
    <circle class="segment-icon-solid" cx="606" cy="752" r="8"/>
    <path d="M606,766 L606,800 M606,772 L626,766"/>
    <path d="M630,800 L640,790 L650,800"/>
  </g>
  <g class="segment-icon icon-development">
    <circle cx="405" cy="762" r="26" stroke-dasharray="8 5"/>
    <path d="M396,768 q-10,-22 9,-24 q19,2 9,24 z M398,776 h14 M400,782 h10"/>
  </g>
  <g class="segment-icon icon-benefits">
    <path d="M236,656 v-16 M256,656 v-28 M276,656 v-38"/>
    <path d="M222,630 L250,608 L264,618 L288,596 M276,596 L288,596 L288,608"/>
  </g>
  <g class="segment-icon icon-retention">
    <path d="M222,354 v26 l18,20 M298,354 v26 l-18,20 M236,372 l10,14 M284,372 l-10,14"/>
  </g>

  <!-- segment labels -->
  <text class="segment-label" x="425" y="307">Sustainment</text>
  <text class="segment-label" x="425" y="350">/ Transition</text>
  <text class="segment-label" x="652" y="307">Responsibility</text>
  <text class="segment-label" x="652" y="350">Fixed</text>
  <text class="segment-label" x="795" y="485">Management</text>
  <text class="segment-label" x="805" y="530">&amp; Oversight</text>
  <text class="segment-label" x="792" y="684">Manning</text>
  <text class="segment-label" x="792" y="730">the Team</text>
  <text class="segment-label" x="634" y="855" style="font-size:40px">Training</text>
  <text class="segment-label" x="408" y="834">Professional</text>
  <text class="segment-label" x="408" y="879">Development</text>
  <text class="segment-label" x="262" y="700">Benefits</text>
  <text class="segment-label" x="259" y="448">Retention</text>
  <text class="segment-label" x="259" y="486">/ Quality of</text>
  <text class="segment-label" x="259" y="524">Life</text>

  <!-- tags -->
  <g class="tag tag-approach">
    <rect class="tag-box" x="856" y="143" width="294" height="162" rx="20"/>
    <text class="tag-text" x="1003" y="213" style="font-size:44px">MANAGEMENT</text>
    <text class="tag-text" x="1003" y="268" style="font-size:58px">APPROACH</text>
  </g>
  <g class="tag tag-evaluation">
    <rect class="tag-box" x="726" y="953" width="424" height="212" rx="20"/>
    <text class="tag-text" x="936" y="1050" style="font-size:88px">PROGRAM</text>
    <text class="tag-text" x="936" y="1140" style="font-size:72px">EVALUATION</text>
  </g>
</svg>
</body>
</html>
```